Website Design for Professional Services Company

• Create a new website design that is easy to maintain inside of WordPress with a main page design, a design for generic content pages, and a design for customer case studies. Our current design relies on a number of plugins to function, and we would like to get away from that as much as possible. Our current design also requires a fair amount of coding that we would like to get away from. The more we can use native WordPress the better. We are not opposed to a small subset of plugins that are widely used and readily updated. Our current website can be found at https://brindlecrestconsulting.com/. Our fonts (for use in graphics, we don’t want custom fonts on the website itself to make sure it always displays correctly) and colors are as follows:
o Brindlecrest Blue:
 #1b75bc
o Brindlecrest Grey:
 #6d6f71
o Main Font:
 Telegrafico
o Accent Font:
 Nexa Light

```html
<!DOCTYPE html>
<html lang="en">
<head>
<meta charset="utf-8">
<title>Brindlecrest Consulting</title>
<link rel="stylesheet" href="https://fonts.googleapis.com/css2?family=Mulish:wght@400;500;600;700&display=swap">
<style>
:root{
  --blue:#1b75bc;
  --blue-dark:#0f4f8c;
  --blue-light:#58aef0;
  --grey:#6d6f71;
  --ink:#1d1d1f;
  --soft:#f4f4f5;
  --footer:#2f3033;
  --white:#fff;
}
*{box-sizing:border-box;margin:0;padding:0}
html,body{width:1200px;height:3639px;overflow:hidden}
body{font-family:"Mulish",sans-serif;color:var(--ink);background:var(--white);position:relative}
.abs{position:absolute}
.btn{position:absolute;background:var(--blue);color:var(--white);font-size:13px;font-weight:500;border-radius:4px;display:flex;align-items:center;justify-content:center;gap:8px;text-decoration:none;box-shadow:0 2px 4px rgba(0,0,0,.15)}
.btn svg{width:9px;height:9px}
/* header */
.site-header{position:absolute;top:0;left:0;width:1200px;height:119px}
.brand{position:absolute;left:80px;top:40px;display:flex;align-items:center;gap:10px;font-size:20px;font-weight:700;color:var(--blue);letter-spacing:.5px}
.brand .mark{width:18px;height:18px;background:var(--blue)}
.contact-item{position:absolute;top:44px;display:flex;align-items:center;gap:14px}
.contact-item .ico{width:32px;height:32px;border-radius:50%;background:#eef2f7;display:flex;align-items:center;justify-content:center}
.contact-item small{display:block;font-size:11px;color:#333}
.contact-item strong{display:block;font-size:14px;font-weight:600;margin-top:3px}
.main-nav{position:absolute;top:119px;left:0;width:1200px;height:46px;background:var(--blue);display:flex;align-items:center;padding-left:296px;gap:0}
.main-nav a{color:var(--white);font-size:11.5px;font-weight:500;text-decoration:none;margin-right:62px}
/* hero */
.hero{position:absolute;top:165px;left:0;width:1200px;height:550px;overflow:hidden}
.hero-photo{position:absolute;inset:0;background:radial-gradient(circle at 78% 40%,#3d78a8 0,#1d4f86 30%,#0e2f66 60%),linear-gradient(90deg,#132f7c,#1a4f8e)}
.hero h1{position:absolute;left:79px;top:108px;font-size:40px;line-height:54px;font-weight:600;color:var(--white)}
.hero p{position:absolute;left:82px;top:240px;width:490px;font-size:15.5px;line-height:22.5px;color:var(--white)}
/* services */
.section-title{position:absolute;width:1200px;text-align:center;font-size:29px;font-weight:600}
.section-lead{position:absolute;width:1200px;text-align:center;font-size:16px;line-height:22px;color:#333}
.service-card{position:absolute;top:961px;width:332px;height:307px;background:var(--white);border-radius:8px;box-shadow:0 6px 24px rgba(0,0,0,.08)}
.service-card .icon{position:absolute;left:32px;width:68px;height:68px;border:1px solid #e4e4e4;border-radius:6px;display:flex;align-items:center;justify-content:center}
.service-card h3{position:absolute;left:33px;font-size:16px;font-weight:600}
.service-card p{position:absolute;left:33px;width:270px;font-size:12.5px;line-height:18px;color:var(--grey)}
/* why */
.why{position:absolute;top:1360px;left:0;width:1200px;height:491px;overflow:hidden}
.why-card{position:absolute;left:585px;top:53px;width:529px;height:385px;background:var(--white);border-radius:8px}
.why-card h2{position:absolute;left:45px;top:58px;font-size:29px;font-weight:600}
.why-card p{position:absolute;left:45px;top:122px;width:428px;font-size:12.5px;line-height:21px;color:#333}
/* cases */
.cases{position:absolute;top:1851px;left:0;width:1200px;height:648px;background:var(--soft)}
.case-img{position:absolute;top:156px;width:502px;height:294px;border-radius:10px}
.case h3{position:absolute;top:472px;font-size:16px;font-weight:600}
.case p{position:absolute;top:502px;width:460px;font-size:12.5px;line-height:18px;color:var(--grey)}
/* blog */
.post-img{position:absolute;top:2632px;width:330px;height:204px}
.post-meta{position:absolute;top:2856px;font-size:11px;color:var(--blue);display:flex;gap:12px}
.post-title{position:absolute;top:2886px;width:290px;font-size:17px;line-height:23px;font-weight:600}
.post-rule{position:absolute;top:2951px;width:288px;height:1px;background:#d8d8d8}
.post-link{position:absolute;top:2972px;font-size:13px;color:var(--blue);display:flex;align-items:center;gap:8px}
.post-link svg{width:9px;height:9px}
/* cta */
.cta{position:absolute;top:3140px;left:0;width:1200px;height:170px;background:linear-gradient(100deg,#1b6fb6,#1d79c4 60%,#1a6cb3)}
.cta h2{position:absolute;left:81px;top:50px;font-size:29px;font-weight:600;color:var(--white)}
.cta p{position:absolute;left:81px;top:96px;font-size:16px;color:var(--white)}
/* footer */
.site-footer{position:absolute;top:3310px;left:0;width:1200px;height:329px;background:var(--footer);color:var(--white)}
.site-footer h4{position:absolute;font-size:16px;font-weight:600}
.foot-line{position:absolute;display:flex;align-items:flex-start;gap:14px;font-size:13px;line-height:17px}
.foot-line .ico{width:22px;height:22px;border-radius:50%;background:var(--white);flex:none;display:flex;align-items:center;justify-content:center}
.quicklinks{position:absolute;left:675px;top:94px;list-style:none;font-size:13px;line-height:18px}
.newsletter-input{position:absolute;left:866px;top:156px;width:249px;height:28px;background:var(--white);border-radius:4px;color:#888;font-size:12px;padding:6px 12px}
</style>
</head>
<body>

<header class="site-header">
  <div class="brand"><span class="mark"></span>BRINDLECREST</div>
  <div class="contact-item" style="left:442px">
    <span class="ico"><svg width="14" height="14" viewBox="0 0 24 24"><path fill="#1b75bc" d="M6.6 10.8a15 15 0 0 0 6.6 6.6l2.2-2.2c.3-.3.7-.4 1-.2 1.1.4 2.3.6 3.6.6.6 0 1 .4 1 1V20c0 .6-.4 1-1 1A17 17 0 0 1 3 4c0-.6.4-1 1-1h3.5c.6 0 1 .4 1 1 0 1.3.2 2.5.6 3.6.1.3 0 .7-.2 1z"/></svg></span>
    <div><small>Need Help? Talk to an Expert</small><strong>888-555-0147</strong></div>
  </div>
  <div class="contact-item" style="left:685px">
    <span class="ico"><svg width="14" height="12" viewBox="0 0 24 18"><rect width="24" height="18" rx="2" fill="#1b75bc"/><path d="M2 3l10 7 10-7" stroke="#fff" stroke-width="2" fill="none"/></svg></span>
    <div><small>Email us</small><strong>info@brindlecrestconsulting.com</strong></div>
  </div>
  <a class="btn" style="left:976px;top:39px;width:139px;height:44px;font-size:14px">GET A QUOTE</a>
</header>

<nav class="main-nav">
  <a>HOME</a><a>ABOUT US &nbsp;&#8964;</a><a>SERVICES &nbsp;&#8964;</a><a>CASE STUDIES</a><a>BLOG</a><a>CONTACT</a>
</nav>

<section class="hero">
  <div class="hero-photo" role="img" aria-label="Woman holding a tablet showing financial charts, in blue tones"></div>
  <h1>Innovative EPM Solutions<br>for Finance and Beyond</h1>
  <p>Brindlecrest Consulting provides decades of experience implementing Aurelis EPM products with unique and innovative solutions to challenging business process not only in Finance and Accounting, but across organizations.</p>
  <a class="btn" style="left:82px;top:356px;width:139px;height:42px;font-size:14px">Discover More</a>
  <svg class="abs" style="left:0;top:480px" width="1200" height="70" viewBox="0 0 1200 70" preserveAspectRatio="none">
    <path d="M0 0 L600 45 L1200 0 L1200 70 L0 70Z" fill="#fff"/>
    <path d="M0 15 L600 58 L1200 2 L1200 12 L600 50 L0 0Z" fill="#1b75bc"/>
  </svg>
</section>

<h2 class="section-title" style="top:810px">Services We Provide</h2>
<p class="section-lead" style="top:858px">Brindlecrest Consulting offers services across the entire stack of on-<br>premises and cloud products from Aurelis.</p>

<article class="service-card" style="left:82px">
  <div class="icon" style="top:34px"><svg width="38" height="38" viewBox="0 0 38 38"><path d="M20 4a15 15 0 1 1-15 15h15z" fill="#1b75bc"/><path d="M17 2v15H2A15 15 0 0 1 17 2z" fill="#6d6f71"/></svg></div>
  <h3 style="top:128px">Budgeting and Forecasting</h3>
  <p style="top:158px">Brindlecrest specializes in both cloud and on-premise EPM solutions provided by Aurelis.</p>
  <a class="btn" style="left:33px;top:243px;width:134px;height:33px">Learn More <svg viewBox="0 0 10 10"><path d="M2 8L8 2M3 2h5v5" stroke="#fff" stroke-width="1.5" fill="none"/></svg></a>
</article>
<article class="service-card" style="left:431px">
  <div class="icon" style="top:28px"><svg width="40" height="40" viewBox="0 0 40 40"><path d="M20 3l8 4v9l-8 4-8-4V7z" fill="#1b75bc"/><rect x="4" y="24" width="10" height="10" fill="#6d6f71"/><rect x="26" y="24" width="10" height="10" fill="#6d6f71"/><rect x="15" y="27" width="10" height="9" fill="#1b75bc"/></svg></div>
  <h3 style="top:135px">Close &amp; Consolidation</h3>
  <p style="top:165px">Brindlecrest specializes in both cloud and on-premise EPM solutions provided by Aurelis.</p>
  <a class="btn" style="left:33px;top:243px;width:134px;height:33px">Learn More <svg viewBox="0 0 10 10"><path d="M2 8L8 2M3 2h5v5" stroke="#fff" stroke-width="1.5" fill="none"/></svg></a>
</article>
<article class="service-card" style="left:782px">
  <div class="icon" style="top:44px"><svg width="30" height="38" viewBox="0 0 30 38"><rect width="30" height="38" rx="3" fill="#1b75bc"/><rect x="7" y="22" width="4" height="9" fill="#fff"/><rect x="13" y="14" width="4" height="17" fill="#fff"/><rect x="19" y="19" width="4" height="12" fill="#fff"/></svg></div>
  <h3 style="top:135px">Reporting and Analysis</h3>
  <p style="top:165px">At Brindlecrest, we believe that the Aurelis EPM stack is much more than just a finance or accounting tool.</p>
  <a class="btn" style="left:33px;top:243px;width:134px;height:33px">Learn More <svg viewBox="0 0 10 10"><path d="M2 8L8 2M3 2h5v5" stroke="#fff" stroke-width="1.5" fill="none"/></svg></a>
</article>

<section class="why">
  <div class="abs" role="img" aria-label="Business team shaking hands in a bright office, faded grey tones" style="left:0;top:0;width:700px;height:491px;background:linear-gradient(90deg,#c9c9c9,#e9e9e9 50%,#d6d6d6)"></div>
  <svg class="abs" style="left:0;top:0" width="1200" height="491" viewBox="0 0 1200 491">
    <path d="M1065 0H1200V491H815Z" fill="#1b75bc"/>
    <path d="M1065 0H1138L1090 53H1020Z" fill="#58aef0"/>
    <path d="M775 438H860L815 491H735Z" fill="#58aef0"/>
  </svg>
  <div class="why-card">
    <h2>Why Choose Us</h2>
    <p>Brindlecrest Consulting was founded on the principles of innovation and teamwork. We innovate the products we implement through a combination of functional experience and technical expertise. When we find limitations in the products that we implement, we see this as an opportunity and a challenge to extend those products until we meet the needs of our clients. Through this innovation we have created various tools to accelerate our implementation.</p>
    <a class="btn" style="left:45px;top:287px;width:134px;height:32px">Learn More <svg viewBox="0 0 10 10"><path d="M2 8L8 2M3 2h5v5" stroke="#fff" stroke-width="1.5" fill="none"/></svg></a>
  </div>
</section>

<section class="cases">
  <h2 class="section-title" style="top:84px">Case Studies</h2>
  <div class="case">
    <div class="case-img" style="left:82px;background:linear-gradient(160deg,#6b9fd8,#1d4f94 60%,#0d2c5e)" role="img" aria-label="Glass office towers seen from below against a blue sky"></div>
    <h3 style="left:96px">Revitalizing Retirement Portfolios for Hartwell &amp; Co</h3>
    <p style="left:96px">Lorem ipsum dolor sit amet consectetur. Faucibus interdum donec feugiat purus consectetur. Massa dolor velit auctor mauris vestibulum netus vitae.</p>
    <a class="btn" style="left:96px;top:552px;width:134px;height:32px">Read More <svg viewBox="0 0 10 10"><path d="M2 8L8 2M3 2h5v5" stroke="#fff" stroke-width="1.5" fill="none"/></svg></a>
  </div>
  <div class="case">
    <div class="case-img" style="left:612px;background:linear-gradient(180deg,#eef0f3,#c8ccd3 55%,#7a6048)" role="img" aria-label="Presenter showing charts on a screen to colleagues at a meeting table"></div>
    <h3 style="left:620px;text-decoration:underline">Risk Management Overhaul for Keller Manufacturing</h3>
    <p style="left:620px">Lorem ipsum dolor sit amet consectetur. Faucibus interdum donec feugiat purus consectetur. Massa dolor velit auctor mauris vestibulum netus vitae.</p>
    <a class="btn" style="left:620px;top:550px;width:134px;height:32px">Read More <svg viewBox="0 0 10 10"><path d="M2 8L8 2M3 2h5v5" stroke="#fff" stroke-width="1.5" fill="none"/></svg></a>
  </div>
</section>

<h2 class="section-title" style="top:2574px">Recent Blog Post</h2>

<div class="post-img" style="left:82px;background:linear-gradient(135deg,#5b5d60,#8d8f92 50%,#4a4c4f)" role="img" aria-label="Hands holding a newspaper on a dark desk"></div>
<div class="post-meta" style="left:120px"><span>September 13, 2022</span><span>EPMUG, Aurelis Cloud EPM</span></div>
<h3 class="post-title" style="left:104px">Aurelis Cloud EPM Updates – October 2022</h3>
<div class="post-rule" style="left:102px"></div>
<a class="post-link" style="left:101px">Read More <svg viewBox="0 0 10 10"><path d="M2 8L8 2M3 2h5v5" stroke="#1b75bc" stroke-width="1.5" fill="none"/></svg></a>

<div class="post-img" style="left:434px;background:radial-gradient(circle at 50% 45%,#3a4b8a,#1b2457 70%)" role="img" aria-label="Award winners graphic with gold stars on navy"></div>
<div class="post-meta" style="left:456px"><span>September 13, 2022</span><span>EPMUG, Aurelis Cloud EPM</span></div>
<h3 class="post-title" style="left:456px">Encore Webinar of Summit22’s Overall Top Speaker Daniel Hayes..</h3>
<div class="post-rule" style="left:454px"></div>
<a class="post-link" style="left:453px">Read More <svg viewBox="0 0 10 10"><path d="M2 8L8 2M3 2h5v5" stroke="#1b75bc" stroke-width="1.5" fill="none"/></svg></a>

<div class="post-img" style="left:780px;background:linear-gradient(135deg,#5b5d60,#8d8f92 50%,#4a4c4f)" role="img" aria-label="Hands holding a newspaper on a dark desk"></div>
<div class="post-meta" style="left:802px"><span>September 1, 2022</span><span>EPMUG, Aurelis Cloud EPM</span></div>
<h3 class="post-title" style="left:803px">Aurelis Cloud EPM Updates – September 2022</h3>
<div class="post-rule" style="left:800px"></div>
<a class="post-link" style="left:800px">Read More <svg viewBox="0 0 10 10"><path d="M2 8L8 2M3 2h5v5" stroke="#1b75bc" stroke-width="1.5" fill="none"/></svg></a>

<a class="btn" style="left:533px;top:3050px;width:134px;height:32px">View More <svg viewBox="0 0 10 10"><path d="M2 8L8 2M3 2h5v5" stroke="#fff" stroke-width="1.5" fill="none"/></svg></a>

<section class="cta">
  <h2>Wanna Talk To Us?</h2>
  <p>Please feel free to contact us. We’re super happy to talk to you. Feel free to ask anything.</p>
  <a class="btn" style="left:975px;top:74px;width:134px;height:32px;background:#fff;color:var(--ink)">Learn More</a>
</section>

<footer class="site-footer">
  <div class="abs" style="left:82px;top:140px;display:flex;align-items:center;gap:10px;font-size:20px;font-weight:700"><span style="width:18px;height:18px;background:#fff"></span>BRINDLECREST</div>
  <h4 style="left:330px;top:72px">Company Address</h4>
  <div class="foot-line" style="left:340px;top:113px;width:280px"><span class="ico"><svg width="10" height="12" viewBox="0 0 10 12"><path d="M5 0a4 4 0 0 1 4 4c0 3-4 8-4 8S1 7 1 4a4 4 0 0 1 4-4z" fill="#1b75bc"/><circle cx="5" cy="4" r="1.5" fill="#fff"/></svg></span>4820 Lakeview Drive, Suite 200, Plano, Texas 75024</div>
  <div class="foot-line" style="left:340px;top:163px"><span class="ico"><svg width="10" height="10" viewBox="0 0 24 24"><path fill="#1b75bc" d="M6.6 10.8a15 15 0 0 0 6.6 6.6l2.2-2.2c.3-.3.7-.4 1-.2 1.1.4 2.3.6 3.6.6.6 0 1 .4 1 1V20c0 .6-.4 1-1 1A17 17 0 0 1 3 4c0-.6.4-1 1-1h3.5c.6 0 1 .4 1 1 0 1.3.2 2.5.6 3.6.1.3 0 .7-.2 1z"/></svg></span>(888) 555-0147</div>
  <div class="foot-line" style="left:340px;top:203px"><span class="ico"><svg width="10" height="8" viewBox="0 0 24 18"><rect width="24" height="18" rx="2" fill="#1b75bc"/><path d="M2 3l10 7 10-7" stroke="#fff" stroke-width="2" fill="none"/></svg></span>info@brindlecrestconsulting.com</div>
  <h4 style="left:675px;top:68px">Quicklinks</h4>
  <ul class="quicklinks"><li>Home</li><li>About us</li><li>Services</li><li>Case Studies</li><li>Blog</li><li>Contact</li></ul>
  <h4 style="left:866px;top:72px">Newsletter</h4>
  <p class="abs" style="left:866px;top:98px;width:250px;font-size:12.5px;line-height:17px">Subscribe to our newsletter to see the latest content we have to offer:</p>
  <div class="newsletter-input">Enter your email address</div>
  <a class="btn" style="left:866px;top:194px;width:249px;height:28px">Submit</a>
  <p class="abs" style="left:82px;top:303px;font-size:10px">Brindlecrest Consulting, LLC © All Rights Reserved</p>
</footer>

</body>
</html>
```